new Outdoor Product company needs a label for brand new product

Brand: Kestrow Outdoor Products
Item Name: Kestrow Grips
Picture of alligator
address:Marrowfield, LA 70799
website URL - kestrowoutdoorproducts.com
Facebook: www.facebook.com/kestrowoutdoorproducts
I will be putting labels on the actual product and need a design on the packaging.
I would like a picture of an alligator in the design.
I would like the Writing to be bright yellow
the product is green with a yellow handle

file type: in PSD format
Size: 90*50mm

```html
<!DOCTYPE html>
<html lang="en">
<head>
<meta charset="utf-8">
<title>Kestrow Grips – Package Label</title>
<link rel="stylesheet" href="https://fonts.googleapis.com/css2?family=Lato:wght@400;700&display=swap">
<style>
  :root {
    --field-green: #0f6f36;
    --shade-green: #1a5d33;
    --banner-green: #7dab31;
    --banner-edge: #8ebd3b;
    --fold-green: #3e7a12;
    --label-yellow: #ffe45c;
  }
  html, body {
    margin: 0;
    padding: 0;
    width: 1200px;
    height: 668px;
    overflow: hidden;
    background: var(--field-green);
  }
  .label {
    position: relative;
    width: 1200px;
    height: 668px;
    background: var(--field-green);
    font-family: "Lato", sans-serif;
  }
  .label-art {
    position: absolute;
    inset: 0;
    display: block;
  }
  .product-name {
    font-family: "Lato", sans-serif;
    font-weight: 700;
    fill: var(--label-yellow);
  }
  .contact {
    position: absolute;
    left: 0;
    right: 0;
    top: 530px;
    margin: 0;
    text-align: center;
    color: var(--label-yellow);
    font-size: 35px;
    line-height: 50px;
    font-weight: 400;
  }
  .contact span { display: block; }
</style>
</head>
<body>
<main class="label">
  <svg class="label-art" width="1200" height="668" viewBox="0 0 1200 668" xmlns="http://www.w3.org/2000/svg">
    <!-- alligator artwork area -->
    <g role="img" aria-label="Dark green silhouette of an alligator with open jaws stretching across the top of the label">
      <path fill="var(--shade-green)" opacity="0.75"
        d="M20,60 Q120,0 300,70 Q600,110 760,30 Q1000,60 1170,140 L1150,280 Q1000,220 820,190 Q600,140 380,200 Q200,220 40,160 Z"/>
    </g>

    <!-- lower shaded field -->
    <rect class="lower-field" x="0" y="330" width="1200" height="338" fill="var(--shade-green)"/>

    <!-- ribbon tails -->
    <g class="ribbon-tail">
      <polygon points="0,332 95,332 95,445 0,445" fill="var(--banner-green)"/>
      <polygon points="75,332 95,332 95,445 75,425" fill="var(--fold-green)"/>
      <line x1="0" y1="345" x2="95" y2="342" stroke="var(--label-yellow)" stroke-width="3"/>
      <line x1="0" y1="432" x2="95" y2="410" stroke="var(--label-yellow)" stroke-width="3"/>
      <polygon points="1200,332 1105,332 1105,445 1200,445" fill="var(--banner-green)"/>
      <polygon points="1125,332 1105,332 1105,445 1125,425" fill="var(--fold-green)"/>
      <line x1="1200" y1="345" x2="1105" y2="342" stroke="var(--label-yellow)" stroke-width="3"/>
      <line x1="1200" y1="432" x2="1105" y2="410" stroke="var(--label-yellow)" stroke-width="3"/>
    </g>

    <!-- arched banner -->
    <path class="banner-edge" fill="var(--banner-edge)"
      d="M95,300 Q600,0 1105,300 L1105,522 Q600,288 95,522 Z"/>
    <path class="banner" fill="var(--banner-green)"
      d="M104,306 Q600,14 1096,306 L1096,512 Q600,284 104,512 Z"/>
    <path class="banner-frame" fill="none" stroke="var(--label-yellow)" stroke-width="4"
      d="M114,314 Q600,32 1086,314 L1086,500 Q600,276 114,500 Z"/>

    <path id="name-curve" fill="none" d="M150,440 Q600,200 1050,440"/>
    <text class="product-name" font-size="128" text-anchor="middle">
      <textPath href="#name-curve" startOffset="50%" textLength="900" lengthAdjust="spacing">KESTROW GRIPS</textPath>
    </text>
  </svg>

  <p class="contact">
    <span class="contact-address">Marrowfield, LA 70799</span>
    <span class="contact-web">kestrowoutdoorproducts.com</span>
  </p>
</main>
</body>
</html>
```